International wholesale business needs a business card

We need a business card.

Company Details:
Company Name and logo
Address, Phone number, Website
Employee Details:
Name, Designation, Mobile Number & Email address

Logo file is attached.

```html
<!DOCTYPE html>
<html lang="en">
<head>
<meta charset="utf-8">
<title>Orvela Trading – Business Card</title>
<link href="https://fonts.googleapis.com/css2?family=Playfair+Display:wght@700&family=Montserrat:wght@400;500&display=swap" rel="stylesheet">
<style>
  :root {
    --bg: #e6e7e8;
    --red: #c3262f;
    --red-back: #c1343a;
    --ink: #333333;
    --white: #ffffff;
  }
  * { margin: 0; padding: 0; box-sizing: border-box; }
  html, body { width: 1048px; height: 1200px; overflow: hidden; background: var(--bg); }
  .canvas { position: relative; width: 1048px; height: 1200px; }
  .card {
    position: absolute; width: 843px; height: 481px; overflow: hidden;
    box-shadow: 0 6px 24px rgba(0,0,0,0.22);
  }
  .card--front { left: 84px; top: 87px; background: var(--white); }
  .card--back { left: 77px; top: 623px; background: var(--red-back); }

  .brand { position: absolute; font-family: 'Playfair Display', serif; font-weight: 700; }
  .brand__name { display: block; line-height: 1; }
  .brand__sub { display: block; line-height: 1; }

  .card--front .brand { left: 38px; top: 78px; color: var(--red); }
  .card--front .brand__name { font-size: 72px; }
  .card--front .brand__sub { font-size: 18px; letter-spacing: 15px; margin: 6px 0 0 108px; }

  .person { position: absolute; left: 38px; top: 219px; font-family: 'Montserrat', sans-serif; color: var(--ink); }
  .person__name { font-family: 'Playfair Display', serif; font-weight: 700; font-size: 38px; color: var(--red); letter-spacing: -1.5px; line-height: 1; }
  .person__role { font-size: 21px; margin-top: 6px; line-height: 1.2; }
  .contact { list-style: none; margin-top: 10px; font-size: 20px; }
  .contact li { display: flex; align-items: center; height: 30px; }
  .contact svg { width: 20px; height: 20px; margin-right: 20px; flex: none; }
  .address { margin-top: 12px; font-size: 21px; line-height: 32px; }

  .card--back .mark { position: absolute; left: 160px; top: 193px; }
  .card--back .brand { left: 300px; top: 200px; color: var(--white); }
  .card--back .brand__name { font-size: 98px; }
  .card--back .brand__sub { font-size: 26px; letter-spacing: 21px; margin: 2px 0 0 152px; }
</style>
</head>
<body>
<main class="canvas">
  <section class="card card--front" aria-label="Card front">
    <div class="brand">
      <span class="brand__name">ORVELA</span>
      <span class="brand__sub">TRADING</span>
    </div>
    <div class="person">
      <h1 class="person__name">MARCUS HALE</h1>
      <p class="person__role">Managing Director</p>
      <ul class="contact">
        <li>
          <svg viewBox="0 0 24 24" aria-hidden="true"><path fill="var(--red)" d="M6.6 10.8a15 15 0 0 0 6.6 6.6l2.2-2.2a1 1 0 0 1 1-.25 11.4 11.4 0 0 0 3.6.57 1 1 0 0 1 1 1V20a1 1 0 0 1-1 1A17 17 0 0 1 3 4a1 1 0 0 1 1-1h3.5a1 1 0 0 1 1 1c0 1.25.2 2.45.57 3.6a1 1 0 0 1-.25 1z"/></svg>
          055-987 654 321
        </li>
        <li>
          <svg viewBox="0 0 24 24" aria-hidden="true"><rect x="2" y="5" width="20" height="14" fill="var(--red)"/><path d="M2 5l10 8 10-8" fill="none" stroke="#fff" stroke-width="1.6"/></svg>
          hello@orvela.com
        </li>
        <li>
          <svg viewBox="0 0 24 24" aria-hidden="true"><circle cx="12" cy="12" r="10" fill="var(--red)"/><path d="M7 8c2 0 3 1 3 3s2 2 2 4-1 3-1 4M14 5c0 2 2 2 3 3s2 3 1 5" fill="none" stroke="#fff" stroke-width="1.5"/></svg>
          www.orvelatrade.com
        </li>
      </ul>
      <p class="address">18, Harbour Row<br>Portland, 97201</p>
    </div>
  </section>

  <section class="card card--back" aria-label="Card back">
    <svg class="mark" width="96" height="96" aria-hidden="true">
      <circle cx="48" cy="48" r="48" fill="var(--white)"/>
    </svg>
    <div class="brand">
      <span class="brand__name">ORVELA</span>
      <span class="brand__sub">TRADING</span>
    </div>
  </section>
</main>
</body>
</html>
```